LITTLE DESIGN WORK REQUIRED!

UPDATE: WE WEREN'T OVERLY ECSTATIC WITH THE DESIGNS WE WERE RECEIVING SO WE DID MOST OF THE DESIGN WORK OURSELVES...

PLEASE SEE THE NEWLY ATTACHED PPT DOC TO VIEW NEARLY EXACT REPLICAS OF WHAT WE WANT THE SITE TO LOOK LIKE. WE NOW NEED YOUR HELP TO MAKE IT LOOK LIKE SOMETHING WORTHY OF THE WEB.

NO CODING REQUIRED - EXPECTED OUTPUT PSD FILES

Hi everyone!

We're looking for a designer to work their magic for our site! We're a not-for-profit program aimed at helping young people realise their potential!

In the attached PPT file, you'll notice we've already DESIGNED THE ENTIRE SITE IN POWERPOINT. Now, we need YOU to make the small changes we requested in the document as well as design the whole thing in psd.

Any questions, don't hesitate to ask.

Brook-Rise
Updates

We've done about 95% of the design for you. Please fine-tune it. See the newly attached PPT doc for details. 

The best two designs will win. This project closes on Friday - please message us if you are absolutely sure you cannot make the deadline.

Thanks,
Brook-Rise

```html
<!DOCTYPE html>
<html lang="en">
<head>
<meta charset="utf-8">
<title>Brook-Rise</title>
<link href="https://fonts.googleapis.com/css2?family=Arimo:ital,wght@0,400;0,700;1,400;1,700&family=PT+Sans:ital,wght@0,400;0,700;1,700&family=Alfa+Slab+One&display=swap" rel="stylesheet">
<style>
:root{
  --bg:#1c331c;
  --page:#ffffff;
  --ink:#1a1a1a;
  --green:#39b82e;
  --fb:#3b5998;
  --blue-title:#3a5a9c;
  --discover:#1565b8;
  --design:#e07416;
  --build:#d3161a;
  --achieve:#35b42b;
  --line:#d8d8d8;
  --footer-top:#6c6c6c;
  --footer-bot:#3c3c3c;
  --hero-a:#5574a8;
  --hero-b:#5f7f4e;
}
*{box-sizing:border-box;margin:0;padding:0}
html,body{width:1200px;height:2271px;overflow:hidden}
body{background:radial-gradient(ellipse at 50% 40%,#24401f,var(--bg));font-family:"Arimo",Arial,sans-serif;color:var(--ink);position:relative}
.page{position:absolute;left:110px;top:0;width:980px;height:2226px;background:var(--page)}
.abs{position:absolute}
/* header */
.brand{left:19px;top:30px;display:flex;align-items:center;gap:10px}
.brand-dot{width:28px;height:28px;border-radius:50%;background:var(--green)}
.brand-name{font-weight:700;font-size:38px;color:#222;letter-spacing:-1px}
.quote{left:677px;top:20px;width:250px;color:#8a8a8a;font-style:italic;font-size:20px;line-height:24px}
.quote .mark{position:absolute;font-size:46px;color:#c9c9c9;font-style:normal;font-family:Georgia,serif;line-height:46px}
.quote .open{left:-28px;top:-8px}
.quote .close{left:232px;top:16px}
.share{left:799px;top:80px;width:138px;height:22px;background:var(--fb);color:#fff;font-size:11px;display:flex;align-items:center;gap:5px;padding-left:5px;border:1px solid #29447e}
.share i{width:12px;height:12px;background:#fff;opacity:.85;display:block}
.nav a{position:absolute;top:131px;display:flex;align-items:center;justify-content:center;height:40px;border-radius:7px;background:linear-gradient(#6a6a6a,#454545);color:#fff;font-weight:700;font-size:13px;text-decoration:none}
.nav a.active{background:linear-gradient(#4fd43a,#23b11c)}
/* hero */
.hero{left:17px;top:187px;width:615px;height:339px;border:1px solid #bbb;padding:6px;background:#fff}
.hero-photo{width:100%;height:100%;background:linear-gradient(160deg,var(--hero-a),var(--hero-b))}
.dots{left:18px;top:538px;display:flex;gap:10px}
.dots span{width:16px;height:16px;border-radius:3px;background:var(--green)}
.dots span.off{background:#b8c6b8}
.feats{left:647px;top:187px;width:313px;height:339px;background:linear-gradient(#1fb51a,#17a513);color:#fff;text-align:center;padding:12px 22px 0}
.feats h2{font-family:"Alfa Slab One",serif;font-weight:400;font-size:62px;line-height:70px;letter-spacing:1px}
.feats p{font-weight:700;font-size:45px;line-height:57px;margin-top:6px}
/* welcome */
.welcome{left:17px;top:590px;width:610px}
.welcome h1{font-family:"PT Sans",sans-serif;font-weight:700;font-size:36px;letter-spacing:-1px;color:#111}
.welcome h1 span{color:var(--green)}
.welcome p{font-size:13px;line-height:24px;color:#444;margin-top:8px}
.welcome .more{font-size:11px;color:#555;font-style:italic;margin-top:2px}
/* posts */
.recent-h{left:17px;top:738px;font-size:22px;font-weight:700}
.cat{left:17px;width:539px;height:29px;color:#fff;font-style:italic;font-size:17px;display:flex;justify-content:space-between;align-items:center;padding:0 14px 0 10px}
.cat.discover{background:linear-gradient(#2a7dd0,var(--discover))}
.cat.design{background:linear-gradient(#f08a2a,var(--design))}
.cat.build{background:linear-gradient(#ea2a2a,var(--build))}
.cat.achieve{background:linear-gradient(#4cc840,var(--achieve))}
.post{width:253px}
.post .thumb{height:167px;border:1px solid #444}
.post h3{font-size:22px;font-weight:700;margin-top:12px}
.post p{font-size:12px;font-style:italic;line-height:18px;margin-top:3px;width:165px}
.t-study{background:linear-gradient(135deg,#7aa14d,#b8ad85)}
.t-summit{background:linear-gradient(160deg,#3f78d0,#123a8a)}
.t-book{background:linear-gradient(135deg,#2a2a2a,#bdbdbd)}
.t-runner{background:linear-gradient(100deg,#d8c9a8,#6f8a3a)}
.t-meeting{background:linear-gradient(135deg,#dfe5ea,#5a6068)}
/* sidebar */
.splash{left:571px;top:662px;width:455px;height:530px;background:radial-gradient(ellipse at 55% 50%,rgba(70,85,150,.55),rgba(70,85,150,.25) 45%,rgba(70,85,150,0) 70%)}
.stay{left:664px;top:556px;font-size:37px;font-weight:700;color:var(--blue-title)}
.like{left:668px;top:617px;display:flex;gap:8px;font-size:11px;color:#333;line-height:13px}
.like b{display:inline-block;border:1px solid #9aa6c0;background:#eceef5;color:var(--fb);padding:3px 6px;font-size:11px;height:22px}
.like i{display:inline-block;width:13px;height:13px;background:var(--fb);margin-right:3px;vertical-align:-2px}
.activity{left:668px;top:708px;width:290px;height:363px;background:#fff;border:1px solid #b5bfd6}
.activity header{height:36px;background:linear-gradient(#5572ae,var(--fb));color:#fff;display:flex;justify-content:space-between;align-items:center;padding:0 10px;font-weight:700}
.activity header .rt{font-size:13px}
.activity header .name{font-size:20px}
.act-item{display:flex;gap:10px;padding:14px 8px 4px}
.act-item i{width:32px;height:32px;background:linear-gradient(#5b78b5,#2f4c8c);flex:none}
.act-item b{display:block;color:var(--fb);font-size:11px;line-height:13px}
.act-item span{color:#999;font-size:10px}
.activity footer{position:absolute;bottom:0;left:0;right:0;height:24px;border-top:1px solid #ddd;font-size:11px;color:#888;display:flex;align-items:center;gap:6px;padding-left:8px}
.activity footer i{width:12px;height:12px;background:var(--fb)}
.box{border:1px solid #9dc27a;background:#fff}
.popular{left:647px;top:1198px;width:311px;height:271px}
.popular header{height:34px;background:linear-gradient(#62c23a,#3b9a1e);color:#fff;font-family:"PT Sans",sans-serif;font-weight:700;font-style:italic;font-size:20px;padding:3px 12px}
.popular ol{list-style:none;padding:10px 12px 0 16px}
.popular li{font-size:13px;line-height:15px;height:36px;display:flex;flex-direction:column}
.popular li b{margin-right:8px}
.popular li em{font-style:normal;font-size:9px;color:#aaa;align-self:flex-end}
.know{left:647px;top:1484px;width:311px;height:534px;text-align:center}
.know h2{font-size:22px;color:#777;font-weight:700;margin-top:6px}
.member{position:absolute;left:0;width:100%}
.member .photo{width:113px;height:128px;margin:0 auto;border:1px solid #ccc}
.member h3{font-size:22px;font-weight:700;margin-top:12px}
.member p{font-size:11px;font-style:italic;line-height:18px;margin-top:3px}
.m-john .photo{background:linear-gradient(#e2e6ea,#6a7480)}
.m-jane .photo{background:linear-gradient(#9cc6e0,#c64050)}
.sep{position:absolute;left:20px;right:20px;top:278px;height:1px;background:var(--line);box-shadow:0 2px 4px rgba(0,0,0,.08)}
/* footer */
.footer{left:0;top:2048px;width:980px;height:178px;background:linear-gradient(var(--footer-top),var(--footer-bot));color:#fff;font-size:13px;line-height:25px}
.footer ul{list-style:none;position:absolute;left:17px;top:22px}
.contact{position:absolute;left:157px;top:22px}
.contact h4{font-size:14px;font-weight:700}
.phones{position:absolute;left:310px;top:47px}
.search{position:absolute;left:640px;top:15px;display:flex;gap:4px}
.search span{width:234px;height:27px;background:#fff;color:#aaa;font-size:11px;padding-left:6px;line-height:27px}
.search b{width:91px;height:27px;background:linear-gradient(#9ed63a,#6fb81c);color:#fff;font-size:12px;text-align:center;line-height:27px;border-radius:4px}
.bottom{left:110px;top:2226px;width:980px;height:38px;background:#8cc63a;color:#fff;font-size:12px;display:flex;justify-content:space-between;align-items:center;padding:0 60px 0 17px}
</style>
</head>
<body>
<div class="page">
  <div class="abs brand"><span class="brand-dot"></span><span class="brand-name">Brook-Rise</span></div>
  <div class="abs quote"><span class="mark open">“</span><span class="mark close">”</span><p>What would you do if you<br>knew you could not fail?<br>- R. Hallam</p></div>
  <div class="abs share"><i></i>Share on Friendbook</div>

  <nav class="nav">
    <a class="active" style="left:15px;width:89px">HOME</a>
    <a style="left:117px;width:88px">About Us</a>
    <a style="left:218px;width:89px">Resources</a>
    <a style="left:320px;width:90px">WorkShops</a>
    <a style="left:424px;width:110px">Ambassadors</a>
    <a style="left:547px;width:88px">Feats</a>
  </nav>

  <div class="abs hero"><div class="hero-photo" role="img" aria-label="Landscape photo: elephants on grassland beneath a mountain"></div></div>
  <div class="abs dots"><span></span><span class="off"></span><span></span><span></span></div>
  <div class="abs feats"><h2>FEATS</h2><p>Challenges that dare you to push yourself.</p></div>

  <section class="abs welcome">
    <h1>Welcome to <span>Brook-Rise</span></h1>
    <p><b>Brook-Rise</b> is a not-for-profit program aimed at helping people – especially young people – set and achieve authentic, meaningful, and audacious goals.</p>
    <p class="more">› Read More</p>
  </section>

  <h2 class="abs recent-h">Recent Posts</h2>

  <div class="abs cat discover" style="top:791px"><span>Discover</span><span>?</span></div>
  <article class="abs post" style="left:19px;top:828px"><div class="thumb t-study" role="img" aria-label="Students studying together on the grass"></div><h3>Title A</h3><p>Lorem ipsum dosectetur adipisicing elit, sed do.</p></article>
  <article class="abs post" style="left:301px;top:828px"><div class="thumb t-summit" role="img" aria-label="Person cheering on a summit"></div><h3>Title B</h3><p>Lorem ipsum dosectetur adipisicing elit, sed do.</p></article>

  <div class="abs cat design" style="top:1107px"><span>Design</span><span>?</span></div>
  <article class="abs post" style="left:19px;top:1145px"><div class="thumb t-book" role="img" aria-label="Person in a suit leafing through a book"></div><h3>Title C</h3><p>Lorem ipsum dosectetur adipisicing elit, sed do.</p></article>
  <article class="abs post" style="left:301px;top:1145px"><div class="thumb t-runner" role="img" aria-label="Sprinter racing on a running track"></div><h3>Title D</h3><p>Lorem ipsum dosectetur adipisicing elit, sed do.</p></article>

  <div class="abs cat build" style="top:1425px"><span>Build</span><span>?</span></div>
  <article class="abs post" style="left:19px;top:1463px"><div class="thumb t-meeting" role="img" aria-label="Business team in an office meeting"></div><h3>Title E</h3><p>Lorem ipsum dosectetur adipisicing elit, sed do.</p></article>
  <article class="abs post" style="left:301px;top:1463px"><div class="thumb t-summit" role="img" aria-label="Person cheering on a summit"></div><h3>Title F</h3><p>Lorem ipsum dosectetur adipisicing elit, sed do.</p></article>

  <div class="abs cat achieve" style="top:1745px"><span>Achieve</span><span>?</span></div>
  <article class="abs post" style="left:19px;top:1783px"><div class="thumb t-book" role="img" aria-label="Person in a suit leafing through a book"></div><h3>Title G</h3><p>Lorem ipsum dosectetur adipisicing elit, sed do.</p></article>
  <article class="abs post" style="left:301px;top:1783px"><div class="thumb t-study" role="img" aria-label="Students studying together on the grass"></div><h3>Title H</h3><p>Lorem ipsum dosectetur adipisicing elit, sed do.</p></article>

  <div class="abs splash" role="img" aria-label="Blue ink splash decoration"></div>
  <h2 class="abs stay">Stay In Touch</h2>
  <div class="abs like"><b>Like</b><span><i></i>22 people like this. Be<br>the first of your friends.</span></div>

  <aside class="abs activity">
    <header><span class="rt">Recent Activity</span><span class="name">Friendbook</span></header>
    <div class="act-item"><i></i><div><b>Calling All Entrepreneurs - Come Hack with Us!</b><span>1,891 people shared this.</span></div></div>
    <div class="act-item"><i></i><div><b>Platform Updates: Improved Dev Site, Documentation, and More</b><span>1,866 people shared this.</span></div></div>
    <div class="act-item"><i></i><div><b>Application Roles and Security Features</b><span>1,866 people shared this.</span></div></div>
    <div class="act-item"><i></i><div><b>The Next Step for Friendbook Credits</b><span>3,383 people shared this.</span></div></div>
    <div class="act-item"><i></i><div><b>HTML 5 Games 0.1</b><span>752 people shared this.</span></div></div>
    <footer><i></i>Friendbook Social Plugin</footer>
  </aside>

  <aside class="abs box popular">
    <header>Popular Posts</header>
    <ol>
      <li><span><b>1.</b>Lorem ipsum dolor sit amet, consectur.</span><em>597 view(s)</em></li>
      <li><span><b>2.</b>Adipiscing elit morbi iaculis pretium leo.</span><em>597 view(s)</em></li>
      <li><span><b>3.</b>Eu faucibus urna ultricies non vestibulum.</span><em>597 view(s)</em></li>
      <li><span><b>4.</b>Eget augue quam necest tristique neque.</span><em>597 view(s)</em></li>
      <li><span><b>5.</b>Curabitur semper arcu feugiat mi sceleri.</span><em>597 view(s)</em></li>
      <li><span><b>6.</b>Queue id vehicula sem convall phasellus.</span><em>597 view(s)</em></li>
    </ol>
  </aside>

  <aside class="abs box know">
    <h2>Get To Know Us</h2>
    <div class="member m-john" style="top:45px"><div class="photo" role="img" aria-label="Portrait photo of an ambassador"></div><h3>John Doe</h3><p>Young entrepreneur &amp; ?<br>Brook-Rise Ambassador<br>› Meet John</p></div>
    <div class="sep"></div>
    <div class="member m-jane" style="top:291px"><div class="photo" role="img" aria-label="Photo of a tennis player on court"></div><h3>Jane Smith</h3><p>Professional athlete &amp; ?<br>Brook-Rise Ambassador<br>› Meet John</p></div>
  </aside>

  <footer class="abs footer">
    <ul><li>Home</li><li>About Us</li><li>Resources</li><li>Workshops</li><li>Ambassadors</li><li>Feats</li></ul>
    <div class="contact"><h4>Contact Us</h4>Dan Morley<br>Lot 14 Fenton Street,<br>Ashgrove, SA, 5160<br>PO Box 240,<br>Ashgrove, SA, 5160</div>
    <div class="phones">Phone Work/Mobile: 0400 123 456<br>Phone: 08 8000 4521<br>Fax: 08 8000 4522<br>Email: dan@brookrise.org</div>
    <div class="search"><span>Search</span><b>SEARCH</b></div>
  </footer>
</div>
<div class="abs bottom"><span>© 2012 Brook-Rise. All Rights Reserved.</span><span>Privacy Policy | SiteMap</span></div>
</body>
</html>
```